IT Distribution Wholesale Business Card & Logo Design

I need both logo and a business card that suits our business model, am happy to pay more for great effort put in.
Brevon Orbital Australia Pty Ltd
An IT Distribution / Wholesale company that distributes technology hardwares, softwares, components, etc.
Offer drop ship services for online retailers and supply to Australia-wide.
Based in Sydney Australia.
Design should give impressions of trust and stability.

Slogan: "your one stop technology supplier"
*two-sided name card
*logo + slogan on the back of the card

I don't have much specific requirements, leave it to designers to come up with creative & interesting masterpiece.
The logo and business card comes in first which i would like it to be completed latest by mid of March, we will require a whole redesign of our web pages, banner design, catalogue design later part.

Goodluck & thank you for your effort.

Hello designers,

Busy week, very good return rate on the number of designs and effort put into our business card design.
I thank you all for that.
We will have to extend this project for another week to two to receive more designs and more time for me to post some updates to you all.
We are getting there, i really liked some of the designs sent but just not the perfect masterpiece we are looking for.

Cheers,
Darnell Q.

Target Market(s)

Computer Retailers, Corporate, Schools, Councils.

Industry/Entity Type

Business

Requirements
Must have
• Brevon Orbital (Australia) Pty Ltd, Darnell Quist, Managing Director, Unit C, 14-18 Pellham Road, Dunmore NSW 2461, Ph +61 2 5037 1942, M +61 4 70395216, E darnell@brevonorbital.com.au, W www.brevonorbital.com.au
Nice to have
• Keep it simple & comfortable.
Target audiences are mostly >30-40 years old range.

Example of companies in the same line:-
http://www.kzp.com.au
http://www.norvix.com.au/
http://www.supplyhaventrade.com/
http://www.quenby.com.au/
http://www.bq456.com.au/
https://www.swiftgridhub.com.au/
http://carvelo.com.au/

```html
<!DOCTYPE html>
<html lang="en">
<head>
<meta charset="utf-8">
<title>Brevon Orbital – Business Card</title>
<link href="https://fonts.googleapis.com/css2?family=Exo+2:wght@300;400;500&display=swap" rel="stylesheet">
<style>
  :root {
    --stage: #2b2b2b;
    --card-dark: #1f2023;
    --card-light: #fdf3df;
    --card-light-edge: #fbe8d8;
    --orange: #f07a1e;
    --amber: #f7a21b;
    --slogan: #c9c9c9;
    --brand-grey: #6f6f73;
    --brand-grey-dark: #5f6064;
    --ink: #2d2d2f;
  }
  * { margin: 0; padding: 0; box-sizing: border-box; }
  html, body { width: 1200px; height: 900px; overflow: hidden; }
  body {
    background: var(--stage);
    font-family: "Exo 2", "Trebuchet MS", sans-serif;
    position: relative;
  }
  .card {
    position: absolute;
    top: 293px;
    width: 516px;
    height: 314px;
    border-radius: 24px;
  }
  .card-back { left: 72px; background: var(--card-dark); }
  .card-front {
    left: 616px;
    background: linear-gradient(120deg, var(--card-light) 0%, #fdf0dc 55%, var(--card-light-edge) 100%);
    overflow: hidden;
  }
  .facet {
    position: absolute;
    inset: 0;
    background:
      linear-gradient(155deg, rgba(255,255,255,0.35) 0 38%, transparent 38%),
      linear-gradient(25deg, transparent 60%, rgba(255,230,205,0.35) 60%);
  }
  .slogan {
    position: absolute;
    top: 46px; left: 0; right: 0;
    text-align: center;
    color: var(--slogan);
    font-size: 16px;
    font-weight: 400;
    letter-spacing: 2.6px;
  }
  .brand-mark {
    position: absolute;
    background: var(--amber);
    border-radius: 4px;
  }
  .card-back .brand-mark { width: 70px; height: 70px; left: 223px; top: 108px; }
  .brand-name, .brand-sub {
    position: absolute;
    text-align: center;
    font-weight: 500;
    text-transform: uppercase;
  }
  .card-back .brand-name, .card-back .brand-sub { left: 0; right: 0; color: var(--brand-grey); }
  .card-back .brand-name { top: 214px; font-size: 27px; letter-spacing: 5px; }
  .card-back .brand-sub { top: 257px; font-size: 13px; letter-spacing: 3px; }

  .card-front .brand-mark { width: 62px; height: 62px; left: 99px; top: 96px; }
  .card-front .brand-name, .card-front .brand-sub { left: 4px; width: 252px; color: var(--brand-grey-dark); }
  .card-front .brand-name { top: 193px; font-size: 20px; letter-spacing: 3px; }
  .card-front .brand-sub { top: 227px; font-size: 11.5px; letter-spacing: 2.4px; }

  .divider {
    position: absolute;
    left: 257px; top: 60px;
    width: 2px; height: 196px;
    background: var(--orange);
  }
  .contact { position: absolute; left: 285px; top: 58px; color: var(--ink); }
  .person-name { color: var(--orange); font-size: 26px; font-weight: 400; line-height: 30px; }
  .person-title { font-size: 14px; line-height: 18px; margin-bottom: 18px; }
  .contact-group { margin-bottom: 14px; }
  .contact-line {
    display: flex; align-items: flex-start; gap: 6px;
    font-size: 14px; line-height: 17px;
  }
  .contact-line svg { flex: none; width: 11px; height: 11px; margin-top: 3px; fill: var(--orange); }
  .indent { padding-left: 17px; }
</style>
</head>
<body>
  <section class="card card-back">
    <p class="slogan">YOUR ONE STOP TECHNOLOGY SUPPLIER</p>
    <div class="brand-mark"></div>
    <p class="brand-name">Brevon Orbital</p>
    <p class="brand-sub">Australia Pty Ltd</p>
  </section>

  <section class="card card-front">
    <div class="facet"></div>
    <div class="brand-mark"></div>
    <p class="brand-name">Brevon Orbital</p>
    <p class="brand-sub">Australia Pty Ltd</p>
    <div class="divider"></div>
    <div class="contact">
      <p class="person-name">Darnell Quist</p>
      <p class="person-title">Managing Director</p>
      <div class="contact-group">
        <p class="contact-line">
          <svg viewBox="0 0 12 12"><path d="M6 0a4 4 0 0 0-4 4c0 3 4 8 4 8s4-5 4-8a4 4 0 0 0-4-4zm0 5.6a1.6 1.6 0 1 1 0-3.2 1.6 1.6 0 0 1 0 3.2z"/></svg>
          <span>Unit C, 14-18 Pellham Road</span>
        </p>
        <p class="contact-line indent">Dunmore NSW 2461</p>
      </div>
      <div class="contact-group">
        <p class="contact-line">
          <svg viewBox="0 0 12 12"><path d="M2.4 0.6l2 2.2-1 1.4c.7 1.6 2 2.9 3.6 3.6l1.4-1 2.2 2-1.2 1.8C5 10.2 1.8 7 1 1.8z"/></svg>
          <span>+61 2 5037 1942</span>
        </p>
        <p class="contact-line">
          <svg viewBox="0 0 12 12"><path d="M3 0h6v12H3zM4 1.2v8.4h4V1.2zM5.5 10.2h1v1h-1z"/></svg>
          <span>+61 4 7039 5216</span>
        </p>
      </div>
      <div class="contact-group">
        <p class="contact-line">
          <svg viewBox="0 0 12 12"><path d="M0 2.5h12v7H0zM0.8 3l5.2 3.6L11.2 3z" /></svg>
          <span>darnell@brevonorbital.com.au</span>
        </p>
        <p class="contact-line">
          <svg viewBox="0 0 12 12"><path d="M6 0a6 6 0 1 0 0 12A6 6 0 0 0 6 0zm0 1.2c.7 0 1.5 1.6 1.7 4.2H4.3C4.5 2.8 5.3 1.2 6 1.2zM1.2 6.6h2.1c.1 1.6.4 3 .9 3.9A4.8 4.8 0 0 1 1.2 6.6zm0-1.2a4.8 4.8 0 0 1 3-3.9c-.5.9-.8 2.3-.9 3.9zm4.8 5.4c-.7 0-1.5-1.6-1.7-4.2h3.4c-.2 2.6-1 4.2-1.7 4.2zm1.8-.3c.5-.9.8-2.3.9-3.9h2.1a4.8 4.8 0 0 1-3 3.9zm.9-5.1c-.1-1.6-.4-3-.9-3.9a4.8 4.8 0 0 1 3 3.9z"/></svg>
          <span>www.brevonorbital.com.au</span>
        </p>
      </div>
    </div>
  </section>
</body>
</html>
```